Stationary & Business cards for Onsite Wastewater Company
Brindlecove Septic Systems Ltd.
Stationary & Business cards for Onsite Wastewater Company - Construction
Creative Brief
Professional
Dwight Amberole
6172 Pellworth St. Harrowfield, N.R. V3K8R2
dwight@brindlecoveseptic-example.com
brindlecoveseptic-example.com
I would like it to say: Design & Build on the front of the card
Open to ideas: maybe use the logo with black background
lanternmoth lanternmoth

```html
<!DOCTYPE html>
<html lang="en">
<head>
<meta charset="utf-8">
<title>Brindlecove Septic Systems Ltd. — Business Card</title>
<link rel="stylesheet" href="https://fonts.googleapis.com/css2?family=Oswald:wght@600&family=Roboto:wght@400;500&display=swap">
<style>
  :root {
    --page: #e9e7e3;
    --ink: #0d0d0d;
    --ink-soft: #2a2a2a;
    --paper: #ffffff;
    --blue: #1e9ad6;
    --blue-deep: #0f6fa8;
    --grey-text: #555555;
    --silver: #d9dcdf;
  }
  * { box-sizing: border-box; margin: 0; padding: 0; }
  html, body {
    width: 1200px; height: 904px; overflow: hidden;
    background: var(--page);
  }
  .sheet { position: relative; width: 1200px; height: 904px; }
  .card {
    position: absolute; left: 250px; width: 700px; height: 400px;
    border-radius: 22px; overflow: hidden;
    box-shadow: 0 10px 26px rgba(0,0,0,0.18);
  }
  .card--back { top: 36px; background: linear-gradient(160deg, var(--ink-soft), var(--ink) 60%); }
  .card--front { top: 468px; background: var(--paper); }

  .brand-name {
    font-family: "Oswald", sans-serif; font-weight: 600;
    text-transform: uppercase; letter-spacing: 1px; line-height: 1.05;
  }
  .card--back .brand { position: absolute; left: 0; right: 0; top: 140px; text-align: center; }
  .card--back .brand-name { color: var(--silver); font-size: 54px; }
  .card--back .brand-sub { color: var(--silver); font-size: 27px; letter-spacing: 3px; }

  .front-art { position: absolute; inset: 0; }
  .holder-name {
    position: absolute; right: 40px; top: 26px;
    font-family: "Roboto", sans-serif; font-size: 20px; color: var(--paper);
  }
  .card--front .brand { position: absolute; left: 36px; top: 162px; }
  .card--front .brand-name { color: var(--ink); font-size: 40px; }
  .card--front .brand-sub { color: var(--ink); font-size: 20px; letter-spacing: 2px; }
  .tagline {
    margin-top: 6px;
    font-family: "Oswald", sans-serif; font-weight: 600;
    font-size: 22px; letter-spacing: 3px; color: var(--blue-deep); text-transform: uppercase;
  }
  .contact {
    position: absolute; left: 400px; top: 166px; list-style: none;
    font-family: "Roboto", sans-serif; font-size: 14px; color: var(--grey-text); line-height: 21px;
    white-space: nowrap;
  }
  .contact li { display: flex; align-items: center; gap: 8px; }
  .contact .icon { width: 12px; height: 12px; flex: none; }
</style>
</head>
<body>
<main class="sheet">
  <section class="card card--back" aria-label="Card back">
    <div class="brand">
      <div class="brand-name">Brindlecove</div>
      <div class="brand-name brand-sub">Septic Systems Ltd.</div>
    </div>
  </section>

  <section class="card card--front" aria-label="Card front">
    <svg class="front-art" width="700" height="400" viewBox="0 0 700 400" aria-hidden="true">
      <path d="M0 0 H700 V72 C520 70 250 80 0 140 Z" fill="var(--ink)"/>
      <path d="M0 140 C250 80 520 70 700 72 V86 C520 84 260 96 0 156 Z" fill="var(--blue)"/>
      <path d="M0 160 C260 100 520 92 700 94 V98 C520 96 260 106 0 166 Z" fill="var(--blue-deep)"/>
      <path d="M0 330 C220 380 480 372 700 330 V400 H0 Z" fill="var(--ink)"/>
      <path d="M0 316 C220 366 480 360 700 318 V330 C480 372 220 380 0 330 Z" fill="var(--blue)"/>
    </svg>
    <div class="holder-name">Dwight Amberole</div>
    <div class="brand">
      <div class="brand-name">Brindlecove</div>
      <div class="brand-name brand-sub">Septic Systems Ltd.</div>
      <div class="tagline">Design &amp; Build</div>
    </div>
    <ul class="contact">
      <li>6172 Pellworth St.</li>
      <li>Harrowfield, N.R., V3K8R2</li>
      <li><svg class="icon" viewBox="0 0 12 12"><rect x="1" y="1" width="10" height="10" rx="2" fill="none" stroke="var(--blue)" stroke-width="1.5"/></svg>555-210-0142</li>
      <li><svg class="icon" viewBox="0 0 12 12"><rect x="1" y="1" width="10" height="10" rx="2" fill="var(--blue)"/></svg>555-210-0178</li>
      <li><svg class="icon" viewBox="0 0 12 12"><rect x="1" y="2" width="10" height="8" rx="1" fill="none" stroke="var(--blue)" stroke-width="1.5"/><path d="M1 3 L6 7 L11 3" fill="none" stroke="var(--blue)" stroke-width="1.2"/></svg>dwight@brindlecoveseptic-example.com</li>
      <li><svg class="icon" viewBox="0 0 12 12"><circle cx="6" cy="6" r="5" fill="none" stroke="var(--blue)" stroke-width="1.5"/></svg>brindlecoveseptic-example.com</li>
    </ul>
  </section>
</main>
</body>
</html>
```